Radical T-shirt Company Shopify Site

I would like to have a a Shopify site designed (and built) for my new t-shirt company. The company is called Jolly Clan and will feature t-shirt designs focused on different characters doing extreme sports. The brand has a mellow and slightly comical feel. We will feature different artists designs as different collections of the brand.
We do not have a logo yet, but we do have some of the sample designs from the artists that we will be featuring on the site. This will give a feel for the branding and style of the site. As far as colors go, I am not sure if a dark theme or light theme will be best. Please use your best judgement for initial designs. Our t-shirt designs are simple and typically line-art style.
It is important to keep in mind that we have several artists that we will feature and that we want to showcase all of them equally until we can understand which will be most popular. Our sites should speak to audiences of all ages. Light, mellow, and slightly comical describe our brand. The site should catch the audiences eye and allow them to see multiple products so they are more likely to buy multiple products.

Expected deliverables:
1. Jolly Clan Wear website (focused on mobile device viewing)- including landing page, multiple collections, product pages, variable colors and sized for shirts and other products, about page, contact page, cart with upsells, subscription package functionality, mailing list pop-up, chat support widget, promo codes, payment collection via stripe- All features should be tested and functioning properly before launch. The site must also be set up to A/B test different products, variations, and upsells.
2. Jolly Nana Website (Focused on mobile site viewing) - Should follow the same branding (with a different logo but in the same coloring and style as the Jolly Clan). This should essentially be a copy of the Jolly Clan website include landing page, multiple collections, product pages, variable colors and sized for shirts and other products, about page, contact page, cart with upsells, subscription package functionality, mailing list pop-up, chat support widget, promo codes, payment collection via stripe- Again, this is a duplicate of the Jolly Clan website, but with a different landing page tuned to Jolly Nana gear.
3. Coding and development of these sites - with the input of 20-30 products (images, descriptions, pricing provided)

I will provide:
1. Examples of products to help with branding and design of the site
2. Feedback on the site
3. All product information for addition to the site
4. Shopify and plugin credentials or access as needed
5. Ongoing work if this goes well

Looking forward to seeing everyone's designs!

Target Market(s)

People that would wear shirts with our characters; grandmas, grandpas, moms, dads, kids, pet lovers- pretty much anyone who enjoys a bit of humor and a nice shirt.

Industry/Entity Type

Comical yet high end t-shirts

Coding

Coded - Design and coding required

Font styles to use
Sans Serif

Requirements
Must have
• Mobile device optimized, Collections carousel on landing page, upsells, features, other recent order popups for users viewing the site, mailing list popup, coupon codes
Nice to have
• Elegant yet playful feel, branding that instills trust and a quick buy.

```html
<!DOCTYPE html>
<html lang="en">
<head>
<meta charset="utf-8">
<title>Jolly Clan Wear</title>
<link href="https://fonts.googleapis.com/css2?family=Poppins:wght@300;400;500;600;700;800&display=swap" rel="stylesheet">
<style>
:root{
  --red:#e30613;
  --dark:#262626;
  --darker:#161616;
  --ink:#1c1c1c;
  --grey:#ebebeb;
  --muted:#7a7a7a;
  --white:#fff;
  --faint:#dedede;
}
*{margin:0;padding:0;box-sizing:border-box}
html,body{width:1200px;height:3965px;overflow:hidden}
body{position:relative;font-family:'Poppins',sans-serif;color:var(--ink);background:var(--white)}
.abs{position:absolute}
.btn{position:absolute;display:flex;align-items:center;justify-content:center;border-radius:20px;font-size:11px;font-weight:700;text-transform:uppercase;height:37px}
.btn-red{background:var(--red);color:var(--white)}
.btn-ghost{border:2px solid #8a8a8a;color:var(--white)}
.eyebrow{position:absolute;font-size:14px;font-weight:700;letter-spacing:8px;text-transform:uppercase}
.h2{position:absolute;font-size:30px;font-weight:700;text-transform:uppercase}
.body-text{position:absolute;font-size:12px;line-height:21px;color:var(--muted)}
.big-num{position:absolute;font-size:110px;font-weight:800;color:var(--faint);line-height:1}
.photo{position:absolute}

/* hero */
.hero-bg{position:absolute;left:0;top:0}
.brand{position:absolute;left:211px;top:42px;color:var(--white);font-weight:700;font-size:22px;line-height:1;display:flex;align-items:center;gap:8px}
.brand .mark{width:12px;height:12px;border-radius:50%;background:var(--white)}
.nav{position:absolute;left:477px;top:52px;display:flex;gap:32px;font-size:12px;color:var(--white)}
.nav .active{color:var(--red);text-decoration:underline}
.search{position:absolute;left:766px;top:46px;width:135px;height:30px;border:1px solid #9a9a9a;border-radius:15px;color:var(--white);font-size:11px;padding:7px 16px}
.icon-dot{position:absolute;width:28px;height:28px;border-radius:50%;background:var(--red);top:47px}
.hero-title{position:absolute;left:211px;top:256px;color:var(--white);font-size:48px;font-weight:800;line-height:56px;text-transform:uppercase}
.hero-text{position:absolute;left:211px;top:376px;width:360px;color:#e6e6e6;font-size:12px;line-height:21px}
.review{position:absolute;z-index:2;left:624px;top:231px;width:196px;height:107px;border:1px solid #8a8a8a;background:rgba(40,40,40,.75);padding:14px 14px;color:var(--white)}
.review .who{display:flex;align-items:center;gap:10px;font-size:9px;font-weight:600}
.review .av{width:24px;height:24px;border-radius:50%;background:#c9a98e}
.review .stars{margin-left:auto;color:#f5b400;font-size:10px;letter-spacing:1px}
.review p{font-size:8.5px;font-style:italic;line-height:16px;margin-top:8px;color:#ddd}
.quote{position:absolute;z-index:3;left:780px;top:218px;color:var(--red);font-size:56px;font-weight:800;font-style:italic;line-height:1}

/* story */
.frame{position:absolute;left:223px;top:777px;width:312px;height:400px;border:3px solid var(--red)}
.story-back{position:absolute;left:249px;top:749px;width:315px;height:397px;background:#e5e5e5}

/* shop */
.tabs{position:absolute;left:400px;top:1449px;width:398px;height:30px;border-radius:15px;background:var(--white);display:flex;align-items:center;font-size:10.5px;color:var(--muted);overflow:hidden}
.tabs span{flex:1;text-align:center;border-left:1px solid #ddd}
.tabs .on{flex:0 0 85px;background:var(--red);color:var(--white);height:100%;display:flex;align-items:center;justify-content:center;font-weight:700;border:0}
.product{position:absolute;width:175px;text-align:center}
.product .shot{width:140px;height:162px;margin:15px auto 0}
.product .kind{font-size:11px;margin-top:24px}
.product .name{font-size:12px;font-weight:700;margin-top:10px;text-transform:uppercase}
.product.featured{background:var(--red);color:var(--white);height:338px}
.rating{font-size:9px;margin-top:6px}
.rating b{color:#ffcb2b;letter-spacing:2px;font-weight:400}
.rating u{margin-left:4px}
.price{font-size:14px;font-weight:700;margin-top:8px}
.price s{font-size:11px;font-weight:400;margin-right:6px}
.shop-btn{margin:12px auto 0;width:146px;height:36px;border-radius:18px;background:var(--white);color:var(--ink);font-size:11px;font-weight:700;display:flex;align-items:center;justify-content:center}

/* sale */
.sale-card{position:absolute;width:365px;height:558px}
.sale-small{position:absolute;font-size:18px;line-height:24px;text-transform:uppercase}
.sale-small b{font-weight:700}
.sale-big{position:absolute;font-size:70px;font-weight:800;line-height:68px;text-transform:uppercase}

/* cta */
.cta-title{position:absolute;left:211px;top:2856px;color:var(--white);font-size:30px;font-weight:700;line-height:37px;text-transform:uppercase}
.cta-text{position:absolute;left:211px;top:2940px;width:450px;color:#e6e6e6;font-size:12px;line-height:21px}

/* blog */
.blog{position:absolute;top:3234px;width:246px;height:322px;background:var(--white);box-shadow:0 4px 18px rgba(0,0,0,.1);padding:11px}
.blog .pic{height:146px}
.blog h3{font-size:17px;line-height:22px;font-weight:700;margin-top:15px}
.blog .meta{font-size:7.5px;margin-top:10px;color:var(--muted)}
.blog .meta i{color:var(--red);font-style:normal}
.blog p{font-size:10.5px;line-height:18px;margin-top:8px;color:var(--muted)}
.blog .more{font-size:10.5px;font-weight:700;margin-top:8px}
.blog.featured{background:var(--red);color:var(--white)}
.blog.featured .meta,.blog.featured p,.blog.featured .meta i{color:#ffe3e3}

/* footer */
.footer{position:absolute;left:0;top:3622px;width:1200px;height:343px;background:var(--darker);color:var(--white)}
.foot-brand{position:absolute;left:211px;top:86px;font-size:27px;font-weight:700;line-height:1;display:flex;align-items:center;gap:10px}
.foot-brand .mark{width:14px;height:14px;border-radius:50%;background:var(--white)}
.foot-about{position:absolute;left:211px;top:144px;width:230px;font-size:12px;line-height:21px;color:#ddd}
.foot-col{position:absolute;top:88px;font-size:12px;color:#ddd}
.foot-col h4{font-size:13px;font-weight:700;color:var(--white);margin-bottom:10px;text-transform:uppercase}
.foot-col li{list-style:none;line-height:27.5px}
.contact-row{display:flex;gap:14px;align-items:flex-start;line-height:14px;margin-bottom:24px}
.social{position:absolute;top:216px;width:26px;height:26px;border-radius:50%;background:var(--red)}
.copy{position:absolute;left:0;top:292px;width:1200px;height:51px;background:#242424;font-size:10.5px;font-weight:600;padding:0 212px;display:flex;align-items:center;justify-content:space-between}
.copy em{color:var(--red);font-style:normal}
</style>
</head>
<body>

<!-- HERO -->
<svg class="hero-bg" width="1200" height="669" viewBox="0 0 1200 669" aria-hidden="true">
  <defs><linearGradient id="heroShade" x1="0" y1="0" x2="1" y2="1"><stop offset="0" stop-color="#333"/><stop offset="1" stop-color="#1f1f1f"/></linearGradient></defs>
  <polygon points="0,0 1200,0 1200,566 0,669" fill="url(#heroShade)"/>
  <polygon points="880,578 1148,567 1148,626 880,626" fill="var(--red)"/>
  <rect x="0" y="234" width="200" height="2" fill="var(--red)"/>
</svg>
<div class="brand"><span class="mark"></span>JOLLY CLAN</div>
<nav class="nav"><span class="active">Home</span><span>Shop</span><span>Our Story</span><span>Contact</span></nav>
<div class="search">Search
  <svg class="abs" style="right:14px;top:8px" width="12" height="12" viewBox="0 0 12 12"><circle cx="5" cy="5" r="3.6" fill="none" stroke="#fff" stroke-width="1.6"/><line x1="7.6" y1="7.6" x2="11" y2="11" stroke="#fff" stroke-width="1.6"/></svg>
</div>
<div class="icon-dot" style="left:920px"><svg width="28" height="28" viewBox="0 0 28 28"><circle cx="14" cy="11" r="3" fill="#fff"/><path d="M9 19a5 4 0 0 1 10 0z" fill="#fff"/></svg></div>
<div class="icon-dot" style="left:960px"><svg width="28" height="28" viewBox="0 0 28 28"><path d="M8 9h2l2 8h7l2-6H11" fill="none" stroke="#fff" stroke-width="1.5"/><circle cx="13" cy="20" r="1.2" fill="#fff"/><circle cx="18" cy="20" r="1.2" fill="#fff"/></svg></div>

<div class="eyebrow" style="left:211px;top:226px;color:#fff">Welcome to Jolly Clan</div>
<h1 class="hero-title">Collection &amp;<br>Style for life</h1>
<p class="hero-text">Lorem ipsum dolor sit amet, consectetur adipiscing elit sed do eiusmod tempor incididunt ut labore.</p>
<a class="btn btn-red" style="left:211px;top:439px;width:147px">Shop now</a>
<a class="btn btn-ghost" style="left:366px;top:439px;width:148px">Learn more</a>

<div class="photo" role="img" aria-label="Man in sunglasses wearing a white Jolly Nana line-art t-shirt" style="left:785px;top:140px;width:230px;height:452px;border-radius:110px 110px 0 0;background:linear-gradient(180deg,#6b5646 0%,#e8e8e8 28%,#d9d9d9 100%)"></div>
<div class="review">
  <div class="who"><span class="av"></span>Sam Reed<span class="stars">★★★★★</span></div>
  <p>Lorem ipsum dolor sit amet, consectetur adipiscing elit, sed do eiusmod tempor incididunt ut labore</p>
</div>
<div class="quote">"</div>

<!-- STORY -->
<div class="story-back"></div>
<div class="frame"></div>
<div class="photo" role="img" aria-label="Man wearing a white Jolly Nana graphic t-shirt outdoors" style="left:237px;top:761px;width:312px;height:400px;background:linear-gradient(180deg,#9aa6a0 0%,#d4d4d0 40%,#b9b3aa 100%)"></div>
<div class="abs" style="left:549px;top:811px;width:66px;height:2px;background:var(--red)"></div>
<div class="eyebrow" style="left:632px;top:803px">Our story</div>
<h2 class="h2" style="left:632px;top:838px">Jolly Clan Gear</h2>
<p class="body-text" style="left:632px;top:885px;width:370px">Lorem ipsum dolor sit amet, consectetur adipiscing elit, sed do eiusmod tempor incididunt ut labore et dolore magnaa aliqua. Quis ipsum suspendisse ultrices gravida. Risusta raf commodo viverra maecenas accumsan lacus vel facilisisa. Lorem ipsum dolor sit amet.</p>
<p class="body-text" style="left:632px;top:1013px;width:370px">Lorem ipsum dolor sit amet, consectetur adipiscing elit,se sed do eiusmod tempor incididunt ut labore</p>
<div class="big-num" style="left:964px;top:1012px">01</div>
<a class="btn btn-red" style="left:632px;top:1076px;width:146px">Learn more</a>

<!-- SHOP -->
<svg class="abs" style="left:0;top:1249px" width="1200" height="706" viewBox="0 0 1200 706" aria-hidden="true">
  <polygon points="0,0 1200,0 1200,640 0,706" fill="var(--grey)"/>
  <polygon points="646,664 1148,646 1148,676 646,676" fill="var(--red)"/>
</svg>
<div class="eyebrow" style="left:0;width:1200px;text-align:center;top:1311px">Our shop</div>
<h2 class="h2" style="left:0;width:1200px;text-align:center;top:1343px">New arrivals</h2>
<p class="body-text" style="left:400px;top:1393px;width:400px;text-align:center">Lorem ipsum dolor sit amet, consectetur adipiscing elit, sed do eiusmod tempor incididunt ut labore et dolore.</p>
<div class="big-num" style="left:183px;top:1374px">02</div>
<div class="tabs"><span class="on">ALL</span><span style="border:0">Women</span><span>Men</span><span>Kids</span><span>Grandparents</span></div>

<div class="product" style="left:210px;top:1523px">
  <div class="shot" role="img" aria-label="White hoodie with line-art print" style="background:radial-gradient(circle,#d8d8d8 40%,transparent 72%)"></div>
  <div class="kind">Lorem ipsum</div><div class="name">Jolly Clan - Hoodie</div>
</div>
<div class="product featured" style="left:411px;top:1523px">
  <div class="shot" role="img" aria-label="White t-shirt with line-art print" style="background:radial-gradient(circle,#f4f4f4 42%,transparent 72%)"></div>
  <div class="kind">Lorem ipsum</div><div class="name">Wave Riders - T shirt</div>
  <div class="rating"><b>★★★★★</b> 4.5 <u>20 Reviews</u></div>
  <div class="price"><s>$90.00</s>$50.00</div>
  <div class="shop-btn">SHOP NOW</div>
</div>
<div class="product" style="left:612px;top:1523px">
  <div class="shot" role="img" aria-label="Black t-shirt with line-art print" style="background:radial-gradient(circle,#222 42%,transparent 72%)"></div>
  <div class="kind">Lorem ipsum</div><div class="name">Jolly Clan - T shirt</div>
</div>
<div class="product" style="left:813px;top:1523px">
  <div class="shot" role="img" aria-label="Red t-shirt with line-art print" style="background:radial-gradient(circle,#e5262b 42%,transparent 72%)"></div>
  <div class="kind">Lorem ipsum</div><div class="name">Jolly Clan - T shirt</div>
</div>

<!-- SALE -->
<div class="big-num" style="left:830px;top:1976px;font-size:118px">03</div>
<div class="sale-card" style="left:220px;top:2043px;background:var(--grey)"></div>
<div class="sale-small" style="left:254px;top:2080px">The<br><b>Sale event</b><br>For the<br>Years</div>
<div class="sale-big" style="left:386px;top:2132px;color:var(--red)">Sale<br>Day</div>
<div class="photo" role="img" aria-label="Young man in glasses wearing a pink Jolly Nana hoodie" style="left:170px;top:2277px;width:300px;height:323px;border-radius:150px 150px 0 0;background:linear-gradient(180deg,#3b2b24 0%,#f2bfd6 35%,#e9a9c6 100%)"></div>
<div class="sale-small" style="left:445px;top:2526px"><b>50% off</b><br>On all items</div>

<div class="sale-card" style="left:612px;top:2097px;background:var(--red)"></div>
<div class="photo" role="img" aria-label="Cheerful man in a green Jolly Nana t-shirt and jeans jumping" style="left:800px;top:2222px;width:225px;height:423px;border-radius:110px 110px 0 0;background:linear-gradient(180deg,#263550 0%,#a9d24a 35%,#5b7bb0 75%,#3d5a8c 100%)"></div>
<div class="sale-small" style="left:612px;width:329px;text-align:right;top:2115px;color:#fff">The<br><b>Sale event</b><br>For the<br>Years</div>
<div class="sale-big" style="left:636px;top:2166px;color:#fff">Sale<br>Day</div>
<div class="abs" style="left:646px;top:2441px;color:#fff;font-size:20px;font-weight:700">ONLY IN</div>
<div class="abs" style="left:644px;top:2475px;color:#fff;font-size:49px;font-weight:700">25.00</div>
<div class="sale-small" style="left:637px;top:2582px;color:#fff"><b>50% off</b><br>On all items</div>

<!-- CTA -->
<svg class="abs" style="left:0;top:2773px" width="1200" height="370" viewBox="0 0 1200 370" aria-hidden="true">
  <defs><linearGradient id="ctaShade" x1="0" x2="1"><stop offset="0" stop-color="#2e2e2e"/><stop offset="1" stop-color="#3b3a38"/></linearGradient></defs>
  <polygon points="0,0 1200,0 1200,305 0,365" fill="url(#ctaShade)"/>
  <polygon points="900,314 1148,302 1148,338 900,338" fill="var(--red)"/>
</svg>
<div class="photo" role="img" aria-label="Smiling man in red cap and red t-shirt holding a shipping box" style="left:746px;top:2707px;width:269px;height:385px;border-radius:130px 130px 0 0;background:linear-gradient(180deg,#e3262b 0%,#e8cbb4 22%,#e83232 45%,#d9c09e 70%,#c9a57f 100%)"></div>
<h2 class="cta-title">Get your new collection<br>&amp; style now at your door</h2>
<p class="cta-text">Lorem ipsum dolor sit amet, consectetur adipiscing elit, sed do eiusmod tempor incididunt ut labore et dolore magna aliqua.</p>
<a class="btn btn-red" style="left:211px;top:3004px;width:146px">Learn more</a>

<!-- BLOGS -->
<h2 class="h2" style="left:0;width:1200px;text-align:center;top:3170px">Our blogs</h2>
<article class="blog" style="left:212px">
  <div class="pic" role="img" aria-label="Man in a dark shirt under blue light" style="background:linear-gradient(135deg,#0d1a3a,#1f3f8a)"></div>
  <h3>Lorem Ipsum is simply dummy text</h3>
  <div class="meta"><i>●</i> 125 views &nbsp;|&nbsp; <i>♥</i> 102 likes &nbsp;|&nbsp; <i>●</i> 13 comments</div>
  <p>Lorem ipsum dolor sit amet, consectetur adipiscing elit, sed do</p>
  <div class="more">READ MORE</div>
</article>
<article class="blog featured" style="left:477px">
  <div class="pic" role="img" aria-label="Man in a striped shirt on a city street" style="background:linear-gradient(135deg,#c9b89a,#4b6a5a 55%,#b44a2e)"></div>
  <h3>Lorem Ipsum is simply dummy text</h3>
  <div class="meta"><i>●</i> 125 views &nbsp;|&nbsp; <i>♥</i> 102 likes &nbsp;|&nbsp; <i>●</i> 13 comments</div>
  <p>Lorem ipsum dolor sit amet, consectetur adipiscing elit, sed do</p>
  <div class="more">READ MORE</div>
</article>
<article class="blog" style="left:741px">
  <div class="pic" role="img" aria-label="Man in a white shirt in front of a building" style="background:linear-gradient(135deg,#8aa6c8,#d9cfb8 50%,#6c7a4a)"></div>
  <h3>Lorem Ipsum is simply dummy text</h3>
  <div class="meta"><i>●</i> 125 views &nbsp;|&nbsp; <i>♥</i> 102 likes &nbsp;|&nbsp; <i>●</i> 13 comments</div>
  <p>Lorem ipsum dolor sit amet, consectetur adipiscing elit, sed do</p>
  <div class="more">READ MORE</div>
</article>

<!-- FOOTER -->
<footer class="footer">
  <div class="foot-brand"><span class="mark"></span>JOLLY CLAN</div>
  <p class="foot-about">Lorem Ipsum is simply dummy text of the printing and typesetting industry Lorem Ipsum has been the industry's standard dummy text ever since the 1500s, when an unknown.</p>
  <div class="foot-col" style="left:524px"><h4>Quicks links</h4><ul><li>Home</li><li>About us</li><li>Prices</li><li>Contact Us</li><li>Sign-In</li></ul></div>
  <div class="foot-col" style="left:695px"><h4>Resources</h4><ul><li>Shop</li><li>Latest News</li><li>Contact Us</li></ul></div>
  <div class="foot-col" style="left:847px"><h4>Contact us</h4>
    <div class="contact-row" style="margin-top:14px"><svg width="10" height="14" viewBox="0 0 10 14"><path d="M5 0a5 5 0 0 1 5 5c0 4-5 9-5 9S0 9 0 5a5 5 0 0 1 5-5z" fill="#fff"/><circle cx="5" cy="5" r="2" fill="#161616"/></svg><span>12 Harbor Lane<br>Seaside Town</span></div>
    <div class="contact-row"><svg width="12" height="12" viewBox="0 0 12 12"><path d="M2 0l3 3-1.5 1.5a7 7 0 0 0 4 4L9 7l3 3-2 2C5 12 0 7 0 2z" fill="#fff"/></svg><span>(555) 0142 7788</span></div>
  </div>
  <span class="social" style="left:847px"></span>
  <span class="social" style="left:893px"></span>
  <div class="copy"><span>COPYRIGHT © <em>JOLLY CLAN GEAR</em> ALL RIGHTS RESERVED.</span><span style="font-weight:400">ALL RIGHTS RESERVED.</span></div>
</footer>

</body>
</html>
```